Business Card design for new private practice opening

I need a business card design for my new private practice with my new logo uploaded as a file
On the front the logo
On the back: maybe a small logo somewhere?
Priv. Doz. DDr. Corinna Vestaluk
Fachärztin für Allgemein- & Viszeralchirurgie
Address: xxx
Tel: xxx
Mobil:xxx
Webseite:xxx
Email:xxx

Contact Information for Business Card

See project description above for details

Requirements
Nice to have
• I would like the colors of the logo incorporated into the business card

```html
<!DOCTYPE html>
<html lang="de">
<head>
<meta charset="utf-8">
<title>Vestaluk Chirurgie – Business Card</title>
<link href="https://fonts.googleapis.com/css2?family=Montserrat:wght@600&family=Poppins:wght@600&family=Catamaran:wght@500&display=swap" rel="stylesheet">
<style>
  :root {
    --backdrop: #6a8fb9;
    --card: #ffffff;
    --brand-grey: #858585;
    --brand-teal: #47bbb9;
    --ink: #151515;
    --shadow: rgba(20, 35, 60, 0.55);
  }
  * { margin: 0; padding: 0; box-sizing: border-box; }
  html, body { width: 923px; height: 1200px; overflow: hidden; }
  body { background: var(--backdrop); position: relative; font-family: "Catamaran", sans-serif; }

  .card {
    position: absolute;
    left: 162px;
    width: 570px;
    height: 326px;
    background: var(--card);
    box-shadow: 6px 7px 8px var(--shadow);
    overflow: hidden;
  }
  .card--front { top: 205px; }
  .card--back { top: 648px; }

  .brand-mark {
    position: absolute;
    border: 4px solid var(--brand-grey);
    border-radius: 50%;
  }
  .card--front .brand-mark { left: 94px; top: 106px; width: 114px; height: 114px; }
  .card--back .brand-mark { left: 390px; top: 125px; width: 130px; height: 130px; border-width: 4px; }

  .brand-name {
    position: absolute;
    left: 224px;
    top: 116px;
    font-family: "Montserrat", sans-serif;
    font-weight: 600;
    font-size: 46px;
    line-height: 48px;
    letter-spacing: 0.5px;
    color: var(--brand-grey);
    text-transform: uppercase;
  }

  .holder { position: absolute; left: 47px; top: 44px; }
  .holder-name {
    font-family: "Poppins", sans-serif;
    font-weight: 600;
    font-size: 29px;
    line-height: 36px;
    color: var(--ink);
  }
  .holder-title { font-size: 14.5px; line-height: 18px; color: var(--ink); margin-top: 0; }

  .contact-list { position: absolute; left: 47px; top: 121px; list-style: none; }
  .contact-item {
    display: flex;
    align-items: center;
    height: 24px;
    margin-bottom: 12px;
    font-size: 14.5px;
    color: var(--ink);
  }
  .contact-item svg { width: 24px; height: 24px; margin-right: 17px; flex: none; }
</style>
</head>
<body>

<section class="card card--front" aria-label="Card front">
  <div class="brand-mark"></div>
  <p class="brand-name">Vestaluk<br>Chirurgie</p>
</section>

<section class="card card--back" aria-label="Card back">
  <div class="holder">
    <h1 class="holder-name">Priv. Doz. DDr. Corinna Vestaluk</h1>
    <p class="holder-title">Farcharztin Fur Allegemein &amp; Viszeralchirurgie</p>
  </div>

  <ul class="contact-list">
    <li class="contact-item">
      <svg viewBox="0 0 24 24" fill="none" stroke="#151515" stroke-width="1.6"><path d="M12 22s7-7 7-12a7 7 0 0 0-14 0c0 5 7 12 7 12z"/><circle cx="12" cy="10" r="2.6"/></svg>
      Your Address here St.123
    </li>
    <li class="contact-item">
      <svg viewBox="0 0 24 24" fill="none" stroke="#151515" stroke-width="1.6" stroke-linejoin="round"><path d="M5 3h4l2 5-2.5 1.5a11 11 0 0 0 6 6L16 13l5 2v4a2 2 0 0 1-2 2A17 17 0 0 1 3 5a2 2 0 0 1 2-2z"/></svg>
      1233456677
    </li>
    <li class="contact-item">
      <svg viewBox="0 0 24 24" fill="none" stroke="#151515" stroke-width="1.6"><rect x="6.5" y="2" width="11" height="20" rx="1.5"/><line x1="11" y1="19" x2="13" y2="19"/></svg>
      1233 4566 7799
    </li>
    <li class="contact-item">
      <svg viewBox="0 0 24 24" fill="none" stroke="#151515" stroke-width="1.6"><circle cx="12" cy="12" r="10"/><ellipse cx="12" cy="12" rx="4.5" ry="10"/><line x1="2" y1="12" x2="22" y2="12"/><path d="M4 7h16M4 17h16"/></svg>
      Your website.Here
    </li>
    <li class="contact-item">
      <svg viewBox="0 0 24 24" fill="none" stroke="#151515" stroke-width="1.6" stroke-linejoin="round"><rect x="2" y="5" width="20" height="14" rx="1"/><path d="M2 6l10 7 10-7"/></svg>
      Your@email.com
    </li>
  </ul>

  <div class="brand-mark"></div>
</section>

</body>
</html>
```